Bright LumaTrex & Equipments

I need to create full stationery design for the company; Business Card, Envelop, Letterheads, Calendar and email template.

Our company is specialized in the import and export of nutritional, pharmaceutical and cosmetics in addition to medical equipments.

These is no limitation on how to use colors within the design.

Target Market(s)

Global

Industry/Entity Type

Healthcare

Other font styles liked:
• a font close to logo. Letterhead body text to be different than the address text

Requirements
Nice to have
• We will have multiple locations so it is good to keep space for future addresses.
• Stationary requirements:
• Letterhead: A4
• Envelopes: 3 regular sizes : large, medium and small (i do not know the sizes)
• Colors: extracted from the logo

```html
<!DOCTYPE html>
<html lang="en">
<head>
<meta charset="utf-8">
<title>Bright LumaTrex &amp; Equipments — Stationery</title>
<link rel="stylesheet" href="https://fonts.googleapis.com/css2?family=Arimo:wght@400;700&family=Carlito:wght@400;700&display=swap">
<style>
  :root{
    --backdrop:#a5a5a5;
    --paper:#ffffff;
    --sky:#29a9e1;
    --navy:#1d1a57;
    --ink:#111111;
    --muted:#555555;
    --mark-faint:#dcdde6;
    --font-body:"Carlito", "Calibri", sans-serif;
    --font-brand:"Arimo", "Arial", sans-serif;
  }
  *{margin:0;padding:0;box-sizing:border-box}
  html,body{width:1200px;height:1000px;overflow:hidden}
  body{background:var(--backdrop);position:relative;font-family:var(--font-body)}

  .sheet{position:absolute;background:var(--paper);overflow:hidden}
  .header-band{position:absolute;left:0;top:0;width:100%;display:block}

  /* Letterhead */
  .letterhead{left:70px;top:125px;width:507px;height:717px}
  .brand{position:absolute;font-family:var(--font-brand);font-weight:700;color:var(--sky);
    display:flex;align-items:center;gap:6px;white-space:nowrap}
  .brand-square{display:inline-block;background:var(--navy);border-radius:2px;flex:none}
  .letterhead .brand{right:40px;top:76px;font-size:15px;line-height:1.1;text-align:right}
  .letterhead .brand-square{width:14px;height:14px}

  .letter-body{position:absolute;left:48px;top:132px;width:412px;color:var(--ink);font-size:9.6px;line-height:17.6px}
  .letter-body h2{font-size:10px;font-weight:700;margin-bottom:17px}
  .letter-body p{margin-bottom:17px}
  .sign-off{font-weight:700;margin-bottom:8px}
  .signature{width:130px;height:40px;background:linear-gradient(90deg,#f1f1f1,#e8e8e8);border-radius:3px;margin-bottom:2px}

  .faint-square{position:absolute;background:var(--mark-faint);border-radius:18px;opacity:.9}
  .letterhead .faint-square{left:324px;top:530px;width:210px;height:210px}

  .letter-footer{position:absolute;left:56px;top:690px;display:flex;align-items:center;gap:16px;
    font-family:var(--font-brand);font-size:6.5px;color:#333}
  .contact{display:flex;align-items:center;gap:4px}
  .contact svg{width:8px;height:8px}
  .contact.address{border-left:1px solid var(--navy);padding-left:6px;color:var(--navy)}

  /* Envelope front */
  .envelope-front{left:598px;top:186px;width:568px;height:270px}
  .envelope-front .brand{left:24px;top:88px;font-size:13px}
  .envelope-front .brand-square{width:12px;height:12px}
  .return-address{position:absolute;left:24px;top:124px;font-family:var(--font-brand);font-size:6px;line-height:8px;color:var(--muted)}
  .envelope-front .faint-square{left:442px;top:152px;width:140px;height:140px}

  /* Envelope back */
  .envelope-back{left:598px;top:497px;width:568px;height:268px}
  .flap{position:absolute;left:0;top:0;width:568px;height:70px;display:block}
  .flap-name{position:absolute;left:0;width:100%;top:22px;text-align:center;
    font-family:var(--font-brand);font-weight:700;font-size:12px;color:var(--paper)}
</style>
</head>
<body>

<section class="sheet letterhead" aria-label="Letterhead">
  <svg class="header-band" viewBox="0 0 507 90" height="90" aria-hidden="true">
    <path d="M0 0H507V28C380 16 180 22 0 40Z" fill="var(--sky)"/>
    <path d="M0 40C90 30 200 24 290 22C190 30 90 50 0 78Z" fill="var(--navy)"/>
  </svg>
  <div class="brand"><span class="brand-square"></span>Bright LumaTrex &amp; Equipments</div>

  <div class="faint-square" aria-hidden="true"></div>

  <article class="letter-body">
    <h2>Lorem Ipsum is simply</h2>
    <p>dummy text of the printing and typesetting industry. Lorem Ipsum has been the industry's standard dummy text ever since the 1500s, when an unknown printer took a galley of type and scrambled it to make a type specimen book. It has survived not only five centuries, but also the leap into electronic typesetting, remaining essentially unchanged. It was popularised in the 1960s with the release of Dryletter sheets containing Lorem Ipsum passages, and more recently with desktop publishing software like Folio PageSetter including versions of Lorem Ipsum.</p>
    <p>It is a long established fact that a reader will be distracted by the readable content of a page when looking at its layout. The point of using Lorem Ipsum is that it has a more-or-less normal distribution of letters, as opposed to using 'Content here, content here', making it look like readable English. Many desktop publishing packages and web page editors now use Lorem Ipsum as their default model text, and a search for 'lorem ipsum' will uncover many web sites still in their infancy. Various versions have evolved over the years, sometimes by accident, sometimes on purpose (injected humour and the like).</p>
    <p>Contrary to popular belief, Lorem Ipsum is not simply random text. It has roots in a piece of classical Latin literature from 45 BC, making it over 2000 years old. Harold Vennick, a Latin professor at Ashcombe College in Virginia, looked up one of the more obscure Latin words, consectetur, from a Lorem Ipsum passage,</p>
    <div class="sign-off">Lorem Ipsum</div>
    <div class="signature" role="img" aria-label="Handwritten signature"></div>
    <div class="signer">Lorem Ipsum is a dummy</div>
  </article>

  <footer class="letter-footer">
    <span class="contact"><svg viewBox="0 0 8 8" aria-hidden="true"><circle cx="4" cy="4" r="4" fill="var(--navy)"/><path d="M2.6 2.2l.8.8-.4.5a3 3 0 0 0 1.5 1.5l.5-.4.8.8-.6.6C3.6 5.8 2.2 4.4 2 2.8z" fill="#fff"/></svg>000-417-2265</span>
    <span class="contact"><svg viewBox="0 0 8 8" aria-hidden="true"><circle cx="4" cy="4" r="4" fill="var(--navy)"/><rect x="2.8" y="2" width="2.4" height="4" rx=".4" fill="#fff"/></svg>000-639-4402</span>
    <span class="contact"><svg viewBox="0 0 8 8" aria-hidden="true"><circle cx="4" cy="4" r="4" fill="var(--navy)"/><circle cx="4" cy="4" r="2" fill="none" stroke="#fff" stroke-width=".6"/></svg>www.brightlumatrex.com</span>
    <span class="contact address">4821 Marlow Crescent City Name, LA 60417</span>
  </footer>
</section>

<section class="sheet envelope-front" aria-label="Envelope front">
  <svg class="header-band" viewBox="0 0 568 70" height="70" aria-hidden="true">
    <path d="M0 0H568V28C420 18 200 22 0 36Z" fill="var(--sky)"/>
    <path d="M0 36C100 28 220 22 318 20C210 28 100 42 0 66Z" fill="var(--navy)"/>
  </svg>
  <div class="brand"><span class="brand-square"></span>Bright LumaTrex &amp; Equipments</div>
  <address class="return-address">12 Corran House<br>Westmere Business Park, City Name</address>
  <div class="faint-square" aria-hidden="true"></div>
</section>

<section class="sheet envelope-back" aria-label="Envelope back">
  <svg class="flap" viewBox="0 0 568 70" aria-hidden="true">
    <path d="M0 0H568L545 40C538 52 530 56 515 56H53C38 56 30 52 23 40Z" fill="var(--navy)"/>
  </svg>
  <div class="flap-name">Bright LumaTrex &amp; Equipments</div>
</section>

</body>
</html>
```